Criação de Kit Layout de Posts para Redes Sociais (Facebook, Instagram e etc) para Fotografia
" Sou Geografo e Fotografo, sendo assim, em minhas viagens e expedições faço registos de paisagens naturais com interação humana e quando estou na paisagem urbana, faço registros de paisagem dicotomica (segregação, desigualdade, movimentos sociais...). Estou com um projeto que irei sair de Motohome pelas Américas, retratando o mundo, dai vem o nome do Projeto VELA SERENA. Além de realizar os registros através das fotos (retratos) ou vídeos, também gosto de retratar, analisar e descrever as minhas vivências e, principalmente, o que me fez fazer os registros. "

```html
<!DOCTYPE html>
<html lang="pt-BR">
<head>
<meta charset="UTF-8">
<title>Vela Serena — Post</title>
<link rel="stylesheet" href="https://fonts.googleapis.com/css2?family=Dosis:wght@400;500;600&display=swap">
<style>
  :root {
    --teal: #72c3ab;
    --teal-deep: #63b59d;
    --white: #ffffff;
    --yellow: #f6c437;
    --ink: #2b3a3a;
    --sky-top: #8a9bb7;
    --sky-glow: #f1b98d;
    --mountain: #6c6f93;
    --rock: #8a7466;
  }
  * { margin: 0; padding: 0; box-sizing: border-box; }
  html, body {
    width: 1200px; height: 1200px; overflow: hidden;
    background: var(--teal);
    font-family: "Dosis", sans-serif;
  }
  .post {
    position: relative;
    width: 1200px; height: 1200px;
    background: linear-gradient(135deg, var(--teal) 0%, var(--teal-deep) 100%);
    color: var(--white);
  }
  .brand {
    position: absolute; left: 110px; top: 90px;
    display: flex; flex-direction: column; align-items: center; gap: 14px;
  }
  .brand-dot {
    width: 70px; height: 70px; border-radius: 50%;
    border: 5px solid var(--white);
  }
  .brand-name {
    font-weight: 500; font-size: 40px; letter-spacing: 8px; line-height: 1;
    text-align: center;
  }
  .headline {
    position: absolute; left: 560px; top: 110px;
    padding: 34px 44px 40px 40px;
    font-weight: 500; font-size: 86px; line-height: 1;
    white-space: nowrap;
  }
  .headline::before,
  .headline::after {
    content: ""; position: absolute; width: 60px; height: 60px;
  }
  .headline::before {
    left: 0; top: 0;
    border-top: 5px solid var(--white); border-left: 5px solid var(--white);
  }
  .headline::after {
    right: 0; bottom: 0;
    border-bottom: 5px solid var(--white); border-right: 5px solid var(--white);
  }
  .photo-frame {
    position: absolute; left: 120px; top: 420px;
    width: 600px; height: 660px;
    background: var(--white); padding: 22px;
    box-shadow: 0 6px 18px rgba(0,0,0,0.12);
  }
  .photo {
    width: 100%; height: 100%;
    background:
      linear-gradient(180deg, transparent 55%, var(--rock) 100%),
      linear-gradient(180deg, var(--sky-top) 0%, var(--sky-glow) 30%, var(--mountain) 58%, #545a7d 100%);
  }
  .place-tag {
    position: absolute; left: 650px; top: 935px;
    width: 250px; height: 95px;
    background: var(--yellow); color: var(--ink);
    display: flex; align-items: center; justify-content: center;
    font-weight: 600; font-size: 38px;
    box-shadow: 0 4px 10px rgba(0,0,0,0.15);
  }
  .handle {
    position: absolute; left: 40px; bottom: 40px;
    font-size: 20px; font-weight: 500;
  }
  .location {
    position: absolute; right: 50px; bottom: 36px;
    font-size: 28px; font-weight: 500;
  }
</style>
</head>
<body>
  <main class="post">
    <div class="brand">
      <span class="brand-dot"></span>
      <span class="brand-name">VELA<br>SERENA</span>
    </div>

    <h1 class="headline">A melhor foto<br>da viagem</h1>

    <figure class="photo-frame">
      <div class="photo" role="img" aria-label="Fotografia de viajante de braços abertos no topo de uma montanha rochosa ao pôr do sol, com serras azuladas ao fundo"></div>
    </figure>

    <div class="place-tag">Minas Gerais</div>

    <p class="handle">@velaserena</p>
    <p class="location">Serra da Mantiqueira - MG</p>
  </main>
</body>
</html>
```